HomeBridle business card and stationary design

We are looking for a simple yet elegant design for our mortgage company business card and stationary.

The card should include:
Name (Derek Walsh)
Title (CEO)
Phone Number (614-208-3917)
Address (48 Birchfield Court, Suite 314, Marlow, OH 43952)
Email (email@homebridle-example.com)
"NMLS" i.e. (NMLS 61947)
"Company NMLS" (Company NMLS 472815)

See above

```html
<!DOCTYPE html>
<html lang="en">
<head>
<meta charset="utf-8">
<title>HomeBridle Business Card</title>
<link rel="stylesheet" href="https://fonts.googleapis.com/css2?family=Arimo:wght@400;700&display=swap">
<style>
  :root {
    --backdrop: #e9e9e7;
    --card: #2a2b2f;
    --card-edge: #232428;
    --brand-blue: #1fa3dc;
    --text-light: #e2e2e2;
    --text-muted: #b9babc;
    --emboss: #3a3b40;
  }
  * { box-sizing: border-box; margin: 0; padding: 0; }
  html, body {
    width: 1200px;
    height: 801px;
    overflow: hidden;
    background: var(--backdrop);
    font-family: "Arimo", Arial, sans-serif;
  }
  .sheet {
    width: 1200px;
    height: 801px;
    display: flex;
    align-items: center;
    justify-content: center;
    gap: 40px;
  }
  .card {
    position: relative;
    width: 540px;
    height: 309px;
    background: var(--card);
    border: 1px solid var(--card-edge);
  }
  /* Front */
  .card-front {
    display: flex;
    align-items: center;
    justify-content: center;
  }
  .front-wordmark {
    font-weight: 700;
    font-size: 58px;
    letter-spacing: 0.5px;
    color: var(--emboss);
  }
  /* Back */
  .back-wordmark {
    position: absolute;
    top: 52px;
    left: 0;
    right: 0;
    text-align: center;
    font-weight: 700;
    font-size: 50px;
    color: var(--brand-blue);
  }
  .details {
    position: absolute;
    top: 140px;
    left: 0;
    right: 0;
    display: flex;
    justify-content: center;
    align-items: stretch;
  }
  .person {
    text-align: right;
    padding-right: 16px;
    display: flex;
    flex-direction: column;
    justify-content: flex-end;
    padding-bottom: 6px;
  }
  .person-name {
    font-weight: 700;
    font-size: 18px;
    color: var(--brand-blue);
    letter-spacing: 0.3px;
  }
  .person-title {
    font-size: 15px;
    color: var(--text-light);
    margin-top: 2px;
  }
  .divider {
    width: 1px;
    background: var(--text-light);
    opacity: 0.8;
  }
  .contact {
    padding-left: 16px;
    font-size: 13.5px;
    line-height: 1.45;
    color: var(--text-light);
  }
  .contact-row {
    display: flex;
    align-items: center;
    gap: 7px;
  }
  .contact-row svg { flex: none; }
  .address { margin-top: 2px; }
  .licenses {
    position: absolute;
    bottom: 30px;
    left: 0;
    right: 0;
    text-align: center;
    font-size: 14px;
    color: var(--text-muted);
    word-spacing: 1px;
  }
  .licenses .sep { margin: 0 8px; }
</style>
</head>
<body>
<main class="sheet">
  <section class="card card-front" aria-label="Card front">
    <div class="front-wordmark">HomeBridle</div>
  </section>

  <section class="card card-back" aria-label="Card back">
    <div class="back-wordmark">HomeBridle</div>

    <div class="details">
      <div class="person">
        <div class="person-name">DEREK WALSH</div>
        <div class="person-title">CEO</div>
      </div>
      <div class="divider"></div>
      <div class="contact">
        <div class="contact-row">
          <svg width="12" height="12" viewBox="0 0 24 24" aria-hidden="true">
            <path fill="#1fa3dc" d="M6.6 10.8a15.1 15.1 0 0 0 6.6 6.6l2.2-2.2a1 1 0 0 1 1-.25 11.4 11.4 0 0 0 3.6.57 1 1 0 0 1 1 1V20a1 1 0 0 1-1 1A17 17 0 0 1 3 4a1 1 0 0 1 1-1h3.5a1 1 0 0 1 1 1c0 1.25.2 2.45.57 3.6a1 1 0 0 1-.25 1z"/>
          </svg>
          <span>614-208-3917</span>
        </div>
        <div class="contact-row">
          <svg width="12" height="10" viewBox="0 0 24 18" aria-hidden="true">
            <rect x="0" y="0" width="24" height="18" rx="2" fill="#1fa3dc"/>
            <path d="M1 1.5 12 10 23 1.5" fill="none" stroke="#2a2b2f" stroke-width="2"/>
          </svg>
          <span>email@homebridle-example.com</span>
        </div>
        <div class="address">48 Birchfield Court<br>Suite 314, Marlow, OH 43952</div>
      </div>
    </div>

    <div class="licenses">NMLS 61947<span class="sep">|</span>Company NMLS 472815</div>
  </section>
</main>
</body>
</html>
```